Bright, Fun and hard to forget home inspection business card.

We need a Business card design for a new Home Inspection company. We are building a brand that is bright, fun and easy to remember.

Target Market(s)

Anyone involed in buying and selling of homes.

Industry/Entity Type

Home Inspection

Contact Information for Business Card

Colin Hartwell Owner/Inspector

Wedsite- KestrelHouseCheck.example
Phone: 253-555-0147
Email- ColinHartwell@mailbox.example
WA Lic # 4738

Requirements
Must have
• BQRV LOGO somewhere on card.

```html
<!DOCTYPE html>
<html lang="en">
<head>
<meta charset="utf-8">
<title>Kestrel House Check LLC – Business Card</title>
<link rel="stylesheet" href="https://fonts.googleapis.com/css2?family=Lato:wght@300;400;700;900&display=swap">
<style>
  :root {
    --backdrop: #d6d6d6;
    --card-black: #0b0b0b;
    --brand-orange: #f05a28;
    --ink-white: #ffffff;
    --ink-grey: #bdbdbd;
    --badge-white: #f4f4f4;
  }
  * { box-sizing: border-box; margin: 0; padding: 0; }
  html, body {
    width: 1200px; height: 926px; overflow: hidden;
    background: var(--backdrop);
    font-family: "Lato", sans-serif;
  }
  .canvas {
    position: relative; width: 1200px; height: 926px;
  }
  .card {
    position: absolute; left: 250px; width: 700px; height: 400px;
    background: var(--card-black);
    overflow: hidden;
    box-shadow: 0 10px 28px rgba(0,0,0,0.28);
  }
  .card--front { top: 43px; }
  .card--back { top: 483px; }
  .card__band {
    position: absolute; inset: 0; width: 700px; height: 400px;
  }
  .band-fill { fill: var(--brand-orange); }

  .brand {
    position: absolute; display: flex; align-items: center; gap: 14px;
    color: var(--ink-white); font-weight: 900; text-transform: uppercase;
    line-height: 1.02;
  }
  .brand__dot {
    flex: none; border-radius: 50%; background: var(--brand-orange);
  }
  .card--front .brand { left: 0; right: 0; top: 92px; justify-content: center; font-size: 40px; }
  .card--front .brand__dot { width: 58px; height: 58px; }
  .card--back .brand { left: 36px; top: 86px; width: 270px; font-size: 30px; }
  .card--back .brand__dot { width: 44px; height: 44px; }

  .front__web {
    position: absolute; left: 0; right: 0; bottom: 22px;
    text-align: center; color: var(--ink-white);
    font-size: 19px; font-weight: 700; letter-spacing: 3px;
  }

  .divider {
    position: absolute; left: 318px; top: 56px; width: 1px; height: 190px;
    background: rgba(255,255,255,0.12);
  }
  .contact {
    position: absolute; left: 345px; top: 62px; color: var(--ink-white);
  }
  .contact__name { font-size: 31px; font-weight: 700; }
  .contact__role { font-size: 17px; font-weight: 300; color: var(--ink-grey); margin-top: 2px; }
  .contact__list { list-style: none; margin-top: 26px; }
  .contact__item {
    display: flex; align-items: center; gap: 10px;
    font-size: 19px; margin-bottom: 9px;
  }
  .contact__icon { width: 20px; height: 20px; flex: none; }

  .credential {
    position: absolute; left: 40px; bottom: 34px;
    display: flex; align-items: center; gap: 22px;
    color: var(--ink-white); font-size: 24px; font-weight: 400; letter-spacing: 0.5px;
  }
  .credential__badge {
    width: 54px; height: 64px; background: var(--badge-white); border-radius: 2px;
  }
</style>
</head>
<body>
<main class="canvas">

  <section class="card card--front" aria-label="Business card front">
    <svg class="card__band" viewBox="0 0 700 400" aria-hidden="true">
      <path class="band-fill" d="M0,318 C230,300 470,322 700,338 L700,400 L0,400 Z"/>
    </svg>
    <div class="brand">
      <span class="brand__dot"></span>
      <span class="brand__name">Kestrel House<br>Check LLC</span>
    </div>
    <p class="front__web">www.KestrelHouseCheck.example</p>
  </section>

  <section class="card card--back" aria-label="Business card back">
    <svg class="card__band" viewBox="0 0 700 400" aria-hidden="true">
      <path class="band-fill" d="M0,262 C230,240 470,300 700,388 L700,400 L0,400 Z"/>
    </svg>
    <div class="brand">
      <span class="brand__dot"></span>
      <span class="brand__name">Kestrel House<br>Check LLC</span>
    </div>
    <div class="divider"></div>
    <div class="contact">
      <h1 class="contact__name">Colin Hartwell</h1>
      <p class="contact__role">Owner/Inspector</p>
      <ul class="contact__list">
        <li class="contact__item">
          <svg class="contact__icon" viewBox="0 0 20 20" aria-hidden="true">
            <rect width="20" height="20" rx="4" fill="#fff"/>
            <path d="M6 4.5 L8 4.5 L9 7.5 L7.6 8.6 C8.3 10.2 9.8 11.7 11.4 12.4 L12.5 11 L15.5 12 L15.5 14 C15.5 15 14.6 15.6 13.6 15.5 C8.8 15 5 11.2 4.5 6.4 C4.4 5.4 5 4.5 6 4.5 Z" fill="#0b0b0b"/>
          </svg>
          <span>253-555-0147</span>
        </li>
        <li class="contact__item">
          <svg class="contact__icon" viewBox="0 0 20 20" aria-hidden="true">
            <rect width="20" height="20" rx="4" fill="#fff"/>
            <rect x="4" y="6" width="12" height="8.5" fill="none" stroke="#0b0b0b" stroke-width="1.6"/>
            <path d="M4 6 L10 11 L16 6" fill="none" stroke="#0b0b0b" stroke-width="1.6"/>
          </svg>
          <span>ColinHartwell@mailbox.example</span>
        </li>
        <li class="contact__item">
          <svg class="contact__icon" viewBox="0 0 20 20" aria-hidden="true">
            <rect width="20" height="20" rx="4" fill="#fff"/>
            <circle cx="10" cy="10" r="6" fill="none" stroke="#0b0b0b" stroke-width="1.5"/>
            <ellipse cx="10" cy="10" rx="2.6" ry="6" fill="none" stroke="#0b0b0b" stroke-width="1.3"/>
            <path d="M4 10 H16" stroke="#0b0b0b" stroke-width="1.3"/>
          </svg>
          <span>www.KestrelHouseCheck.example</span>
        </li>
      </ul>
    </div>
    <div class="credential">
      <span class="credential__badge" role="img" aria-label="BQRV certification badge"></span>
      <span>WA Lic # 4738</span>
    </div>
  </section>

</main>
</body>
</html>
```